Marlowvane Services Website Design

We have most content but require a professional design. We have a logo already and will need it utilized along with several of the photos from the attached documentation.
First page should have our mission and Vision and the synapsis provided in the word document. Visitors will be prompted to select from one of our 3 divisions from this page.
Each division will have the same list of tabs : About, Services, Safety, Careers and Contact.
Photos on each divisions page should be representative of the divisions offerings. The word doc attached contains the requested content and we are open to edits that would complement and fill the website.
I like the Tornwick site www.tornwick-example.com - they are our competition so cant be modeled directly after this.
Please include prompts to request quote at each service page. align the format of the geotechnical page to the other 2 divisions.
I used chat gpt for some of the content so will need it optimized for SCO.

```html
<!DOCTYPE html>
<html lang="en">
<head>
<meta charset="utf-8">
<title>Marlowvane Services</title>
<link href="https://fonts.googleapis.com/css2?family=Orbitron:wght@500;600;700&family=Roboto:wght@400;500&display=swap" rel="stylesheet">
<style>
:root{
  --red:#e81c24;
  --black:#000;
  --ink:#1a1a1a;
  --white:#fff;
  --blush:#fcf1f0;
  --line:#e5e5e5;
}
*{box-sizing:border-box;margin:0;padding:0}
html,body{width:1200px;height:2976px;overflow:hidden}
body{position:relative;background:var(--white);font-family:"Roboto",Arial,sans-serif;color:var(--ink)}
.abs{position:absolute}
.display{font-family:"Orbitron",sans-serif;text-transform:uppercase}

/* header */
.site-header{position:absolute;left:0;top:0;width:1200px;height:84px;background:var(--white)}
.brand{position:absolute;left:100px;top:26px;font-family:"Orbitron",sans-serif;font-weight:700;font-size:27px;color:var(--red);letter-spacing:1px}
.main-nav{position:absolute;left:482px;top:33px;display:flex;gap:29px}
.main-nav a{font-family:"Orbitron",sans-serif;font-size:14px;font-weight:500;color:var(--ink);text-decoration:none;text-transform:uppercase}
.btn-contact{position:absolute;left:961px;top:20px;width:141px;height:46px;border-radius:23px;background:var(--red);color:var(--white);font-family:"Orbitron",sans-serif;font-size:14px;font-weight:600;display:flex;align-items:center;justify-content:center;box-shadow:0 3px 6px rgba(0,0,0,.25)}

/* hero */
.hero{position:absolute;left:0;top:84px;width:1200px;height:600px;background:linear-gradient(180deg,#4a4a3e 0%,#6b5a45 30%,#8a6d50 60%,#7a5f46 100%)}
.hero-panel{position:absolute;left:288px;top:144px;width:626px;height:312px;background:rgba(0,0,0,.82);border-bottom:7px solid var(--red);text-align:center}
.hero-title{margin-top:58px;font-family:"Orbitron",sans-serif;font-weight:700;font-size:46px;line-height:69px;color:var(--white)}
.btn-start{display:inline-flex;align-items:center;justify-content:center;margin-top:12px;width:157px;height:45px;border-radius:23px;background:var(--red);color:var(--white);font-family:"Orbitron",sans-serif;font-size:14px;font-weight:600}

/* headings */
.section-title{position:absolute;left:0;width:1200px;text-align:center;font-family:"Orbitron",sans-serif;font-weight:600;font-size:28px;color:var(--ink)}

/* service cards */
.service-card{position:absolute;width:310px;height:253px;border-radius:10px;overflow:hidden;display:flex;flex-direction:column;align-items:center;justify-content:center;text-align:center;color:var(--white);font-size:21px;font-weight:500;line-height:32px;padding:0 30px}
.service-card::after{content:"";display:block;width:42px;height:3px;background:var(--white);margin-top:12px}
.service-card.small{font-size:17px}

/* vision / mission */
.statement{position:absolute;top:1492px;width:463px;height:357px;border-radius:14px;text-align:center;color:var(--white);padding:40px 34px 0}
.statement h2{font-family:"Orbitron",sans-serif;font-weight:600;font-size:27px;margin:6px 0 16px}
.statement p{font-size:15.5px;line-height:31px}
.vision{left:114px;background:var(--red)}
.mission{left:620px;background:var(--black)}

/* divisions */
.divisions{position:absolute;left:0;top:1957px;width:1200px;height:573px;background:var(--blush)}
.division-photo{position:absolute;width:309px;height:241px}
.division-icon{position:absolute;width:78px;height:67px;background:var(--red);display:flex;align-items:center;justify-content:center}
.division-label{position:absolute;width:290px;background:var(--white);box-shadow:0 2px 6px rgba(0,0,0,.12);padding:20px 30px;font-family:"Orbitron",sans-serif;font-size:16px;font-weight:500;line-height:31px;color:var(--ink)}
.division-label.active{border-bottom:5px solid var(--red)}

/* footer */
.site-footer{position:absolute;left:0;top:2530px;width:1200px;height:446px;background:var(--black);color:var(--white)}
.footer-heading{position:absolute;top:63px;font-family:"Orbitron",sans-serif;font-weight:600;font-size:22px}
.quick-links{position:absolute;left:117px;top:113px;list-style:none}
.quick-links li{display:flex;align-items:center;gap:12px;font-size:13.5px;height:31px}
.divider{position:absolute;top:90px;height:238px;border-left:1px dashed #888}
.contact-item{position:absolute;left:372px;width:241px;padding-left:45px}
.contact-item b{display:block;font-size:17px;font-weight:500;margin-bottom:8px}
.contact-item span{font-size:15px}
.contact-item.sep{border-bottom:1px dashed #888}
.icon-dot{position:absolute;left:2px;top:0;width:30px;height:30px;border-radius:50%;background:var(--red);display:flex;align-items:center;justify-content:center}
.field{position:absolute;left:733px;width:353px;height:40px;border:1px solid #ddd;border-radius:2px;font-size:14px;padding:11px 12px}
.btn-submit{position:absolute;left:733px;top:262px;width:353px;height:38px;background:var(--red);font-family:"Orbitron",sans-serif;font-size:14px;font-weight:600;display:flex;align-items:center;justify-content:center}
.social{position:absolute;top:281px;width:27px;height:27px;border-radius:50%;background:var(--red)}
.footer-rule{position:absolute;left:98px;top:388px;width:1004px;border-top:1px solid #888}
.copyright{position:absolute;left:0;top:407px;width:1200px;text-align:center;font-size:14px}
</style>
</head>
<body>

<header class="site-header">
  <div class="brand">MARLOWVANE</div>
  <nav class="main-nav">
    <a href="#">Home</a><a href="#">About Us</a><a href="#">Our Leadership</a><a href="#">Services</a>
  </nav>
  <div class="btn-contact">CONTACT US</div>
</header>

<section class="hero" role="img" aria-label="White aerial lift truck parked on a dirt yard with trees and a building behind">
  <div class="hero-panel">
    <h1 class="hero-title">WELCOME TO<br>MARLOWVANE</h1>
    <div class="btn-start">GET STARTED</div>
  </div>
</section>

<h2 class="section-title" style="top:770px">Marlowvane Services</h2>

<div class="service-card" style="left:98px;top:843px;background:linear-gradient(160deg,#2b3a55,#8a4a4a 55%,#2a3550)" role="img" aria-label="Icebreaker ship at sunset">Delivering safe</div>
<div class="service-card small" style="left:445px;top:843px;background:linear-gradient(160deg,#5b6874,#2f3a42 60%,#1f262c)" role="img" aria-label="Oil and gas refinery pipelines">Reliable aerial access and maintenance services to Oil&amp;Gas,</div>
<div class="service-card" style="left:791px;top:843px;background:linear-gradient(170deg,#2d3d5a,#6b5540 55%,#5a3518)" role="img" aria-label="Construction site with cranes">Construction</div>
<div class="service-card" style="left:273px;top:1134px;background:linear-gradient(160deg,#4a3a2c,#2e2820 55%,#3d3024)" role="img" aria-label="Workers laying utility pipe in a trench">Utility</div>
<div class="service-card" style="left:619px;top:1134px;background:linear-gradient(180deg,#7d8a96,#556069 55%,#4b5a42)" role="img" aria-label="Renewable energy plant towers">Renewable energy industries</div>

<section class="statement vision">
  <svg width="66" height="54" viewBox="0 0 66 54" fill="none" stroke="#fff" stroke-width="2"><path d="M33 12a13 13 0 0 0-8 23v7h16v-7a13 13 0 0 0-8-23z"/><path d="M27 46h12M29 50h8M30 34l3-8 3 8"/><path d="M33 2v5M14 10l4 4M52 10l-4 4M6 26h5M55 26h5M4 32q29 22 58 0"/></svg>
  <h2>OUR VISION</h2>
  <p>To be the leading provider of aerial access, geotechnical drilling, and service solutions, setting the standard for excellence in safety, efficiency, and environmental stewardship.</p>
</section>
<section class="statement mission">
  <svg width="60" height="58" viewBox="0 0 60 58" fill="none" stroke="#fff" stroke-width="2"><rect x="4" y="2" width="38" height="52" rx="3"/><path d="M10 13h7v7h-7zM10 27h7v7h-7zM10 41h7v7h-7zM22 16h14M22 30h12M22 44h8"/><circle cx="46" cy="44" r="11"/><circle cx="46" cy="44" r="6"/><circle cx="46" cy="44" r="1.5"/></svg>
  <h2>OUR MISSION</h2>
  <p>At Marlowvane, our mission is to deliver unparalleled aerial access, geotechnical drilling, and service and maintenance solutions, consistently exceeding our clients' expectations. We strive to achieve this by investing in cutting-edge technology,&nbsp; sustainability.</p>
</section>

<section class="divisions">
  <h2 class="section-title" style="top:88px">Select Division</h2>

  <div class="division-photo" style="left:98px;top:165px;background:linear-gradient(160deg,#1d4f8a,#3a6fa8 45%,#7a6a55)" role="img" aria-label="Aerial access platform above the earth"></div>
  <div class="division-icon" style="left:329px;top:306px"><svg width="38" height="34" viewBox="0 0 38 34" fill="none" stroke="#fff" stroke-width="2"><rect x="2" y="4" width="34" height="22" rx="2"/><circle cx="13" cy="15" r="5"/><path d="M22 11h9M22 17h9M8 30h22"/></svg></div>
  <div class="division-label" style="left:117px;top:373px">AERIAL ACCESS</div>

  <div class="division-photo" style="left:446px;top:165px;background:linear-gradient(180deg,#6a7a92,#e8a050 55%,#5a6a86)" role="img" aria-label="Two workers standing on solar panels at sunset"></div>
  <div class="division-icon" style="left:677px;top:306px"><svg width="40" height="38" viewBox="0 0 40 38" fill="none" stroke="#fff" stroke-width="2"><path d="M4 36V18l9-6v6l9-6v6l9-6v24zM28 12V4h5v32M10 24h4M18 24h4M10 30h4M18 30h4M28 4q4-3 8 0"/></svg></div>
  <div class="division-label active" style="left:465px;top:373px">RENEWABLE ENERGY SERVICES</div>

  <div class="division-photo" style="left:793px;top:165px;background:linear-gradient(160deg,#6a5a48,#8a7256 50%,#5a4a3a)" role="img" aria-label="Drilling rig and excavators on a construction site from above"></div>
  <div class="division-icon" style="left:1024px;top:306px"><svg width="38" height="38" viewBox="0 0 38 38" fill="none" stroke="#fff" stroke-width="2"><circle cx="19" cy="19" r="13"/><path d="M19 2v5M19 31v5M2 19h5M31 19h5M12 24h14v-8l-7-5-7 5z"/></svg></div>
  <div class="division-label" style="left:812px;top:373px">GEOTECHNICAL DRILLING</div>
</section>

<footer class="site-footer">
  <h3 class="footer-heading" style="left:114px">QUICK LINKS</h3>
  <ul class="quick-links">
    <li><svg width="14" height="12" viewBox="0 0 14 12"><path d="M1 6h9M7 2l4 4-4 4" stroke="#fff" stroke-width="2.4" fill="none"/></svg>Home</li>
    <li><svg width="14" height="12" viewBox="0 0 14 12"><path d="M1 6h9M7 2l4 4-4 4" stroke="#fff" stroke-width="2.4" fill="none"/></svg>About Us</li>
    <li><svg width="14" height="12" viewBox="0 0 14 12"><path d="M1 6h9M7 2l4 4-4 4" stroke="#fff" stroke-width="2.4" fill="none"/></svg>Our Leadership</li>
    <li><svg width="14" height="12" viewBox="0 0 14 12"><path d="M1 6h9M7 2l4 4-4 4" stroke="#fff" stroke-width="2.4" fill="none"/></svg>Services</li>
    <li><svg width="14" height="12" viewBox="0 0 14 12"><path d="M1 6h9M7 2l4 4-4 4" stroke="#fff" stroke-width="2.4" fill="none"/></svg>Contact Us</li>
  </ul>
  <div class="social" style="left:102px"></div>
  <div class="social" style="left:147px"></div>
  <div class="social" style="left:190px"></div>
  <div class="social" style="left:235px"></div>

  <div class="divider" style="left:319px"></div>

  <h3 class="footer-heading" style="left:372px">CONTACT DETAILS</h3>
  <div class="contact-item sep" style="top:110px;height:70px">
    <div class="icon-dot"><svg width="14" height="14" viewBox="0 0 14 14"><path d="M3 1l2 3-1.5 1.5a8 8 0 0 0 5 5L10 9l3 2-1.5 2.5C6 13 1 8 .5 2.5z" fill="#fff"/></svg></div>
    <b>Phone;</b><span>+1 555 010 2040</span>
  </div>
  <div class="contact-item sep" style="top:190px;height:72px">
    <div class="icon-dot"><svg width="14" height="11" viewBox="0 0 14 11"><rect width="14" height="11" rx="1.5" fill="#fff"/><path d="M1 1l6 5 6-5" stroke="#e81c24" stroke-width="1.4" fill="none"/></svg></div>
    <b>Email:</b><span>hello@marlowvane-example.com</span>
  </div>
  <div class="contact-item" style="top:276px">
    <div class="icon-dot"><svg width="12" height="15" viewBox="0 0 12 15"><path d="M6 0a6 6 0 0 0-6 6c0 4 6 9 6 9s6-5 6-9a6 6 0 0 0-6-6z" fill="#fff"/><circle cx="6" cy="6" r="2" fill="#e81c24"/></svg></div>
    <b>Address:</b><span>Marlowvane Yard, Harlow Ridge.</span>
  </div>

  <div class="divider" style="left:687px"></div>

  <h3 class="footer-heading" style="left:732px">CONTACT ME</h3>
  <div class="field" style="top:102px">Name:</div>
  <div class="field" style="top:155px">Email:</div>
  <div class="field" style="top:207px">Address:</div>
  <div class="btn-submit">SUBMIT NOW</div>

  <div class="footer-rule"></div>
  <p class="copyright">Copyrights@2023.Marlowvane Services.All Rights Reserved</p>
</footer>

</body>
</html>
```